Awesome Flyer for Tactical Emergency Response Services

We need a Flyer for Emergency Rapid Response services for my company ferncrest Security Services Ltd. , we are a security guisard service based in Trinidad in the Caribbean.
The flyer will include price and pictures of our tactical team. must be clear concise, and strong.

Rapid response services is where customers pay a monthly fee and if they have any security issues they call us and we immediately respond to their home or business to ensure their safety and security.

Target Market(s)

Homeowners; people worried about home security such as home invasions etc.

Requirements
Must have
• Company Logo prominent

```html
<!DOCTYPE html>
<html lang="en">
<head>
<meta charset="utf-8">
<title>Ferncrest Security Services – 24 hr Emergency Rapid Response</title>
<link rel="stylesheet" href="https://fonts.googleapis.com/css2?family=Rubik:wght@500;700&family=Open+Sans:wght@600;700&display=swap">
<style>
  :root {
    --red: #c41e34;
    --red-dark: #a3172a;
    --ink: #4d4d4d;
    --paper: #f7f7f7;
    --paper-shade: #e6e6e6;
    --footer-grey: #c9c9c9;
    --stage: #e4e4e4;
    --white: #ffffff;
  }
  * { margin: 0; padding: 0; box-sizing: border-box; }
  html, body { width: 1200px; height: 2234px; overflow: hidden; }
  body { background: var(--stage); position: relative; font-family: "Open Sans", sans-serif; }

  .flyer {
    position: absolute; left: 0; top: 268px;
    width: 1200px; height: 1698px; overflow: hidden;
    background: linear-gradient(160deg, var(--white) 0%, var(--paper) 55%, var(--paper-shade) 100%);
  }
  .hero { position: absolute; left: 0; top: 0; width: 1200px; height: 960px; }

  .headline {
    position: absolute; left: 0; width: 1200px; top: 938px;
    text-align: center; font-family: "Rubik", sans-serif; font-weight: 700;
    font-size: 55px; color: var(--red); letter-spacing: 0.3px;
  }

  .features { position: absolute; top: 1054px; left: 0; width: 1200px; height: 210px; }
  .feature { position: absolute; top: 0; text-align: center; color: var(--ink); font-weight: 600; font-size: 24px; line-height: 33px; }
  .feature svg { display: block; margin: 12px auto 16px; fill: var(--red); }
  .feature--equipped { left: 82px; width: 380px; }
  .feature--protect { left: 508px; width: 260px; }
  .feature--peace { left: 790px; width: 352px; }
  .divider { position: absolute; top: 0; width: 0; height: 207px; border-left: 3px dashed var(--red); }
  .divider--one { left: 495px; }
  .divider--two { left: 783px; }

  .price {
    position: absolute; top: 1313px; left: 274px; width: 701px; height: 75px;
    background: var(--red); clip-path: polygon(5% 0, 100% 0, 95% 100%, 0 100%);
    color: var(--white); font-family: "Rubik", sans-serif; font-weight: 700;
    font-size: 55px; line-height: 75px; text-align: center;
  }
  .offer { position: absolute; top: 1408px; left: 0; width: 1200px; text-align: center; font-family: "Rubik", sans-serif; font-weight: 700; color: #5a5a5a; }
  .offer-lead { font-size: 38px; line-height: 48px; }
  .offer-terms { font-size: 38px; line-height: 48px; }
  .offer-terms em { font-style: normal; color: var(--red); }

  .footer-band {
    position: absolute; left: 0; top: 1518px; width: 1200px; height: 180px;
    background: linear-gradient(90deg, var(--footer-grey) 0%, #f0f0f0 45%, #d9d9d9 100%);
    clip-path: polygon(0 0, 37% 0, 48% 100%, 0 100%);
  }
  .brand { position: absolute; left: 78px; top: 1584px; display: flex; align-items: center; gap: 16px; }
  .brand-mark { width: 26px; height: 26px; border-radius: 50%; background: var(--red); }
  .brand-name { font-family: "Rubik", sans-serif; font-weight: 500; font-size: 30px; color: var(--red); line-height: 1.1; }

  .contact-bar {
    position: absolute; left: 499px; top: 1559px; width: 701px; height: 111px;
    background: var(--red); clip-path: polygon(0 0, 100% 0, 100% 100%, 11% 100%);
    color: var(--white); font-family: "Rubik", sans-serif; font-weight: 700; font-size: 27px;
  }
  .contact-col { position: absolute; top: 14px; line-height: 42px; }
  .contact-col--phones { left: 84px; }
  .contact-col--web { left: 276px; right: 10px; padding-left: 12px; border-left: 2px solid rgba(255,255,255,0.7); }
  .contact-line { display: flex; align-items: center; gap: 6px; white-space: nowrap; }
  .contact-line svg { flex: none; }
</style>
</head>
<body>
<main class="flyer">
  <svg class="hero" viewBox="0 0 1200 960">
    <defs>
      <linearGradient id="teamPhoto" x1="0" y1="0" x2="0" y2="1">
        <stop offset="0" stop-color="#8c8f88"/>
        <stop offset="0.45" stop-color="#4b4a48"/>
        <stop offset="0.8" stop-color="#4f6a34"/>
        <stop offset="1" stop-color="#557a2f"/>
      </linearGradient>
      <linearGradient id="drillPhoto" x1="0" y1="0" x2="0" y2="1">
        <stop offset="0" stop-color="#a4a39c"/>
        <stop offset="0.55" stop-color="#3f3f3c"/>
        <stop offset="1" stop-color="#5d8035"/>
      </linearGradient>
    </defs>
    <ellipse class="hero-outline" cx="600" cy="130" rx="700" ry="625" fill="none" stroke="var(--red)" stroke-width="4"/>
    <ellipse class="hero-ring-white" cx="600" cy="130" rx="690" ry="615" fill="var(--white)"/>
    <ellipse class="hero-ring" cx="600" cy="130" rx="668" ry="595" fill="var(--red)"/>
    <ellipse class="team-photo" cx="600" cy="130" rx="628" ry="555" fill="url(#teamPhoto)"
      role="img" aria-label="Photo of the tactical response team in uniform and vests standing in front of marked patrol cars"/>
    <circle class="drill-photo" cx="225" cy="575" r="132" fill="url(#drillPhoto)" stroke="var(--red)" stroke-width="8"
      role="img" aria-label="Photo of officers practising a tactical entry along a wall"/>
    <circle class="drill-photo" cx="993" cy="575" r="132" fill="url(#drillPhoto)" stroke="var(--red)" stroke-width="8"
      role="img" aria-label="Photo of the team advancing in formation"/>
    <circle class="drill-photo" cx="608" cy="756" r="153" fill="url(#drillPhoto)" stroke="var(--red)" stroke-width="8"
      role="img" aria-label="Photo of officers detaining a suspect beside a car"/>
  </svg>

  <h1 class="headline">24 hr Emergency Rapid Response</h1>

  <section class="features">
    <div class="feature feature--equipped">
      <svg width="84" height="70" viewBox="0 0 84 70" aria-hidden="true">
        <rect x="32" y="0" width="20" height="9" rx="2"/>
        <path d="M18 12h48l10 22H8z"/>
        <rect x="2" y="32" width="80" height="24" rx="6"/>
        <rect x="8" y="52" width="16" height="16" rx="3"/>
        <rect x="60" y="52" width="16" height="16" rx="3"/>
        <circle cx="16" cy="44" r="5" fill="var(--white)"/>
        <circle cx="68" cy="44" r="5" fill="var(--white)"/>
        <path d="M24 17h36l6 14H18z" fill="var(--white)"/>
      </svg>
      Fully equipped and specially trained in tactical rapid response protocols
    </div>
    <span class="divider divider--one"></span>
    <div class="feature feature--protect">
      <svg width="94" height="70" viewBox="0 0 94 70" aria-hidden="true">
        <path d="M2 35C20 8 74 8 92 35C74 62 20 62 2 35z" fill="none" stroke="var(--red)" stroke-width="7"/>
        <circle cx="47" cy="35" r="17"/>
        <circle cx="41" cy="29" r="5" fill="var(--white)"/>
      </svg>
      Protecting you<br>24/7
    </div>
    <span class="divider divider--two"></span>
    <div class="feature feature--peace">
      <svg width="80" height="70" viewBox="0 0 80 70" aria-hidden="true">
        <circle cx="40" cy="14" r="12"/>
        <circle cx="14" cy="24" r="9"/>
        <circle cx="66" cy="24" r="9"/>
        <rect x="24" y="30" width="32" height="40" rx="8"/>
        <rect x="2" y="37" width="20" height="30" rx="6"/>
        <rect x="58" y="37" width="20" height="30" rx="6"/>
      </svg>
      Delivering Peace<br>of mind to our clients
    </div>
  </section>

  <div class="price">$200 + VAT per month</div>

  <div class="offer">
    <p class="offer-lead">Sign up for</p>
    <p class="offer-terms"><em>12 months</em> and receive a <em>10% discount</em></p>
  </div>

  <div class="footer-band"></div>
  <div class="brand">
    <span class="brand-mark"></span>
    <span class="brand-name">Ferncrest<br>Security Services</span>
  </div>

  <div class="contact-bar">
    <div class="contact-col contact-col--phones">
      <p class="contact-line">
        <svg width="24" height="24" viewBox="0 0 26 26" aria-hidden="true"><circle cx="13" cy="13" r="11" fill="none" stroke="#fff" stroke-width="2"/><path d="M9 7l3 3-2 2c1 2 2 3 4 4l2-2 3 3-2 2c-5 0-10-5-10-10z" fill="#fff"/></svg>
        555-0148
      </p>
      <p class="contact-line">
        <svg width="24" height="24" viewBox="0 0 26 26" aria-hidden="true"><circle cx="13" cy="13" r="11" fill="none" stroke="#fff" stroke-width="2"/><path d="M9 7l3 3-2 2c1 2 2 3 4 4l2-2 3 3-2 2c-5 0-10-5-10-10z" fill="#fff"/></svg>
        555-0162
      </p>
    </div>
    <div class="contact-col contact-col--web">
      <p class="contact-line">
        <svg width="24" height="24" viewBox="0 0 26 26" aria-hidden="true"><circle cx="13" cy="13" r="11" fill="none" stroke="#fff" stroke-width="2"/><rect x="7" y="9" width="12" height="9" fill="none" stroke="#fff" stroke-width="1.8"/><path d="M7 9l6 5 6-5" fill="none" stroke="#fff" stroke-width="1.8"/></svg>
        info@ferncrest-tt.com
      </p>
      <p class="contact-line">
        <svg width="24" height="24" viewBox="0 0 26 26" aria-hidden="true"><circle cx="13" cy="13" r="11" fill="none" stroke="#fff" stroke-width="2"/><circle cx="13" cy="13" r="7" fill="none" stroke="#fff" stroke-width="1.6"/><path d="M6 13h14M13 6v14" stroke="#fff" stroke-width="1.6"/></svg>
        www.ferncrest-tt.com
      </p>
    </div>
  </div>
</main>
</body>
</html>
```